Window Wrap advertising for Insurance Agency
Pinegate Coverage Partners
Window Wrap advertising for Insurance Agency - Financial Services
We are an insurance agency specializing in Auto, Home, Life and Business insurance and we are looking to update the graphics and messaging of some window wraps that we have on our building. We currently have 6 windows wrapped but are now wanting to wrap a total of 8 windows. they are of various sizes, so I am providing an .ai file with the appropriately sized artboards to make things a little easier. The .ai file will also show you what our previous wraps looked like. We do not like anything about our old design, so please do not rely too heavily on it. The windows that these wraps will go on are facing a fairly busy street and we want some messaging on these wraps that will entice potential clients to come in or call us to get insurance quotes. Walk-ins are welcome at our office. We really want to see ideas that are eye-catching, and have a great call to action.
Financial Services
All members of the public who drive cars, own homes, own businesses or need life insurance ( which is to say, almost everyone.)
Velmora Velmora
Hello why you make it unvield? Please make it veild again so that other designer can not see our designs, this is very simportant so that we assure that no one copy other ideas. And please also provide text content for each window. Thanks
tallowk58 tallowk58
Hello designers, Thank you for your submissions. I would like to clarify a few things. First of all, there are a total of 8 windows... In the ai file that I attached, there are 8 art boards. Although there are 3 blank art boards, we need all 8 to be designed. Second, we HATE our current window designs. Please do not use any of the design cues from the current windows. The only logo that we want included somewhere is our own logo which I have also attached. I'd like to reiterate that we want to see eye catching designs that will help draw in traffic. And text on the windows needs to be fairly large so that it can bee seen from the street. If you have questions, please feel free to send me a message. Thanks again for your designs.

```html
<!DOCTYPE html>
<html lang="en">
<head>
<meta charset="utf-8">
<title>Pinegate Coverage Partners – Window Wraps</title>
<link href="https://fonts.googleapis.com/css2?family=Roboto:wght@700&family=Roboto+Condensed:wght@700&display=swap" rel="stylesheet">
<style>
  :root {
    --bg: #000000;
    --cream-top: #f8f5c8;
    --cream-bottom: #ece6a6;
    --maroon: #7c1a22;
    --maroon-dark: #5e1118;
    --orange: #e8782a;
    --blue: #1f8fd0;
    --ink: #111111;
    --white: #ffffff;
  }
  * { margin: 0; padding: 0; box-sizing: border-box; }
  html, body { width: 1200px; height: 923px; overflow: hidden; background: var(--bg); }
  .wraps { position: relative; width: 1200px; height: 923px; }

  .wrap {
    position: absolute;
    background: linear-gradient(180deg, var(--cream-top), var(--cream-bottom));
    overflow: hidden;
    display: flex;
    flex-direction: column;
  }
  .wrap::after {
    content: "";
    position: absolute; left: 0; right: 0; bottom: 0;
    height: 9px; background: var(--maroon);
  }
  .wrap-header { position: relative; height: 88px; flex: none; }
  .wrap-header svg { position: absolute; inset: 0; width: 100%; height: 100%; }
  .brand {
    position: absolute; top: 10px; left: 0; right: 0;
    text-align: center; color: var(--white);
    font-family: "Roboto Condensed", sans-serif; font-weight: 700;
    line-height: 1;
  }
  .brand .brand-top { display: block; font-size: 11px; letter-spacing: 1px; }
  .brand .brand-mid { display: block; font-size: 19px; letter-spacing: 0.5px; }
  .brand .brand-low { display: block; font-size: 8px; letter-spacing: 2px; margin-top: 1px; }

  .wrap-body {
    flex: 1;
    display: flex; flex-direction: column;
    align-items: center; justify-content: center;
    text-align: center; color: var(--ink);
    padding-bottom: 14px;
  }
  .headline {
    font-family: "Roboto", sans-serif; font-weight: 700;
    font-size: 44px; line-height: 1.22; text-transform: uppercase;
  }
  .stack {
    font-family: "Roboto Condensed", sans-serif; font-weight: 700;
    text-transform: uppercase;
  }

  /* positions */
  .home     { left: 40px;  top: 87px;  width: 304px; height: 362px; }
  .life     { left: 369px; top: 87px;  width: 305px; height: 362px; }
  .contact  { left: 709px; top: 87px;  width: 194px; height: 337px; }
  .hours    { left: 931px; top: 87px;  width: 194px; height: 337px; }
  .business { left: 40px;  top: 511px; width: 297px; height: 362px; }
  .auto     { left: 374px; top: 511px; width: 295px; height: 362px; }
  .quotes   { left: 711px; top: 511px; width: 200px; height: 362px; }
  .agents   { left: 948px; top: 511px; width: 205px; height: 362px; }

  .home .wrap-body, .life .wrap-body { padding-top: 50px; }
  .business .wrap-body, .auto .wrap-body { padding-top: 40px; }

  /* contact panel */
  .contact .wrap-body { justify-content: flex-start; padding-top: 34px; }
  .contact-mark {
    width: 62px; height: 62px; border-radius: 50%;
    background: var(--maroon); margin-bottom: 18px;
  }
  .contact-name {
    font-family: "Roboto Condensed", sans-serif; font-weight: 700;
    color: var(--maroon); text-transform: uppercase; line-height: 1;
  }
  .contact-name .n1 { display: block; font-size: 14px; letter-spacing: 1px; }
  .contact-name .n2 { display: block; font-size: 24px; }
  .contact-name .n3 { display: block; font-size: 10px; letter-spacing: 2px; margin-top: 2px; }
  .phone {
    position: absolute; left: 8px; right: 8px; bottom: 16px;
    background: var(--maroon); color: var(--white);
    font-family: "Roboto", sans-serif; font-weight: 700;
    font-size: 27px; text-align: center; padding: 6px 0;
  }

  /* hours panel */
  .hours .wrap-body { padding-top: 10px; }
  .hours-text { font-family: "Roboto", sans-serif; font-weight: 700; font-size: 36px; line-height: 1.2; }
  .site { font-family: "Roboto", sans-serif; font-weight: 700; font-size: 16px; margin-top: 28px; }

  .quotes .stack { font-size: 30px; line-height: 1.45; }
  .quotes .wrap-body { padding-top: 30px; }
  .agents .stack { font-size: 31px; line-height: 1.35; }
  .agents .stack .gap { display: block; height: 22px; }
  .agents .wrap-body { padding-top: 16px; }
</style>
</head>
<body>
<main class="wraps">

  <!-- reusable header markup repeated per panel -->
  <section class="wrap home">
    <div class="wrap-header">
      <svg viewBox="0 0 100 100" preserveAspectRatio="none" aria-hidden="true">
        <polygon points="0,0 100,0 100,48 50,78 0,48" fill="var(--maroon)"/>
        <polyline points="0,62 50,92 100,62" fill="none" stroke="var(--orange)" stroke-width="7"/>
        <polyline points="0,72 50,102 100,72" fill="none" stroke="var(--blue)" stroke-width="6"/>
      </svg>
      <div class="brand"><span class="brand-top">PINEGATE</span><span class="brand-mid">COVERAGE</span><span class="brand-low">PARTNERS</span></div>
    </div>
    <div class="wrap-body"><p class="headline">Home<br>Insurance</p></div>
  </section>

  <section class="wrap life">
    <div class="wrap-header">
      <svg viewBox="0 0 100 100" preserveAspectRatio="none" aria-hidden="true">
        <polygon points="0,0 100,0 100,48 50,78 0,48" fill="var(--maroon)"/>
        <polyline points="0,62 50,92 100,62" fill="none" stroke="var(--orange)" stroke-width="7"/>
        <polyline points="0,72 50,102 100,72" fill="none" stroke="var(--blue)" stroke-width="6"/>
      </svg>
      <div class="brand"><span class="brand-top">PINEGATE</span><span class="brand-mid">COVERAGE</span><span class="brand-low">PARTNERS</span></div>
    </div>
    <div class="wrap-body"><p class="headline">Life<br>Insurance</p></div>
  </section>

  <section class="wrap contact">
    <div class="wrap-header">
      <svg viewBox="0 0 100 100" preserveAspectRatio="none" aria-hidden="true">
        <polygon points="0,0 100,0 100,48 50,78 0,48" fill="var(--maroon)"/>
        <polyline points="0,62 50,92 100,62" fill="none" stroke="var(--orange)" stroke-width="7"/>
        <polyline points="0,72 50,102 100,72" fill="none" stroke="var(--blue)" stroke-width="6"/>
      </svg>
      <div class="brand"><span class="brand-top">PINEGATE</span><span class="brand-mid">COVERAGE</span><span class="brand-low">PARTNERS</span></div>
    </div>
    <div class="wrap-body">
      <div class="contact-mark" aria-hidden="true"></div>
      <p class="contact-name"><span class="n1">Pinegate</span><span class="n2">Coverage</span><span class="n3">Partners</span></p>
    </div>
    <p class="phone">801-555-0147</p>
  </section>

  <section class="wrap hours">
    <div class="wrap-header">
      <svg viewBox="0 0 100 100" preserveAspectRatio="none" aria-hidden="true">
        <polygon points="0,0 100,0 100,48 50,78 0,48" fill="var(--maroon)"/>
        <polyline points="0,62 50,92 100,62" fill="none" stroke="var(--orange)" stroke-width="7"/>
        <polyline points="0,72 50,102 100,72" fill="none" stroke="var(--blue)" stroke-width="6"/>
      </svg>
      <div class="brand"><span class="brand-top">PINEGATE</span><span class="brand-mid">COVERAGE</span><span class="brand-low">PARTNERS</span></div>
    </div>
    <div class="wrap-body">
      <p class="hours-text">Walk-ins<br>Welcome<br>M-F 9-5</p>
      <p class="site">PinegateCoverage.Biz</p>
    </div>
  </section>

  <section class="wrap business">
    <div class="wrap-header">
      <svg viewBox="0 0 100 100" preserveAspectRatio="none" aria-hidden="true">
        <polygon points="0,0 100,0 100,48 50,78 0,48" fill="var(--maroon)"/>
        <polyline points="0,62 50,92 100,62" fill="none" stroke="var(--orange)" stroke-width="7"/>
        <polyline points="0,72 50,102 100,72" fill="none" stroke="var(--blue)" stroke-width="6"/>
      </svg>
      <div class="brand"><span class="brand-top">PINEGATE</span><span class="brand-mid">COVERAGE</span><span class="brand-low">PARTNERS</span></div>
    </div>
    <div class="wrap-body"><p class="headline">Business<br>Insurance</p></div>
  </section>

  <section class="wrap auto">
    <div class="wrap-header">
      <svg viewBox="0 0 100 100" preserveAspectRatio="none" aria-hidden="true">
        <polygon points="0,0 100,0 100,48 50,78 0,48" fill="var(--maroon)"/>
        <polyline points="0,62 50,92 100,62" fill="none" stroke="var(--orange)" stroke-width="7"/>
        <polyline points="0,72 50,102 100,72" fill="none" stroke="var(--blue)" stroke-width="6"/>
      </svg>
      <div class="brand"><span class="brand-top">PINEGATE</span><span class="brand-mid">COVERAGE</span><span class="brand-low">PARTNERS</span></div>
    </div>
    <div class="wrap-body"><p class="headline">Auto<br>Insurance</p></div>
  </section>

  <section class="wrap quotes">
    <div class="wrap-header">
      <svg viewBox="0 0 100 100" preserveAspectRatio="none" aria-hidden="true">
        <polygon points="0,0 100,0 100,48 50,78 0,48" fill="var(--maroon)"/>
        <polyline points="0,62 50,92 100,62" fill="none" stroke="var(--orange)" stroke-width="7"/>
        <polyline points="0,72 50,102 100,72" fill="none" stroke="var(--blue)" stroke-width="6"/>
      </svg>
      <div class="brand"><span class="brand-top">PINEGATE</span><span class="brand-mid">COVERAGE</span><span class="brand-low">PARTNERS</span></div>
    </div>
    <div class="wrap-body"><p class="stack">Free Quotes<br>Save $$<br>Multiple<br>Companies</p></div>
  </section>

  <section class="wrap agents">
    <div class="wrap-header">
      <svg viewBox="0 0 100 100" preserveAspectRatio="none" aria-hidden="true">
        <polygon points="0,0 100,0 100,48 50,78 0,48" fill="var(--maroon)"/>
        <polyline points="0,62 50,92 100,62" fill="none" stroke="var(--orange)" stroke-width="7"/>
        <polyline points="0,72 50,102 100,72" fill="none" stroke="var(--blue)" stroke-width="6"/>
      </svg>
      <div class="brand"><span class="brand-top">PINEGATE</span><span class="brand-mid">COVERAGE</span><span class="brand-low">PARTNERS</span></div>
    </div>
    <div class="wrap-body"><p class="stack">Great<br>Coverage<span class="gap"></span>Experienced<br>Agents</p></div>
  </section>

</main>
</body>
</html>
```